Needs cd cover for Progressive house release project to be used to sell on digital market online, the song and cover will be released on the market between the months of October and November,please the cd cover must include artist/song name (Dj Lumbrix - Velvet Tideway), cover must be at least minimum 2000 x 2000 pixel maximum 3000 x 3000 pixel.

Requirements
Must have
• Artist/Title: Dj Lumbrix - Velvet Tideway
• Cover format: minimum 2000 x 2000 pixel maximum 3000 x 3000 pixel
Nice to have
• Woman on the cover

```html
<!DOCTYPE html>
<html lang="en">
<head>
<meta charset="utf-8">
<title>Dj Lumbrix – Velvet Tideway</title>
<link rel="stylesheet" href="https://fonts.googleapis.com/css2?family=Quicksand:wght@700&display=swap">
<style>
  :root {
    --space-deep: #050a26;
    --space-navy: #0b1a4a;
    --cone-cyan: #3fb3df;
    --cone-light: #7fd8f5;
    --nebula-violet: #5a3aa8;
    --title-white: #ffffff;
    --glow-violet: #a66bff;
    --glow-cyan: #2fd0ff;
  }
  html, body {
    margin: 0;
    padding: 0;
    overflow: hidden;
    background: var(--space-deep);
  }
  .cover {
    position: relative;
    width: 1199px;
    height: 1200px;
    overflow: hidden;
  }
  .cover-art {
    position: absolute;
    inset: 0;
    background:
      radial-gradient(ellipse 28% 22% at 52% 73%, #040818 0%, #071030 70%, transparent 100%),
      radial-gradient(ellipse 48% 36% at 50% 66%, var(--cone-light) 0%, var(--cone-cyan) 55%, #1d5c8e 80%, transparent 100%),
      radial-gradient(ellipse 60% 45% at 50% 30%, rgba(90, 58, 168, 0.55) 0%, transparent 80%),
      radial-gradient(ellipse 70% 60% at 50% 55%, var(--space-navy) 0%, var(--space-deep) 100%);
  }
  .titles {
    position: absolute;
    inset: 0;
    width: 1199px;
    height: 1200px;
  }
  .title {
    font-family: "Quicksand", sans-serif;
    font-weight: 700;
    fill: var(--title-white);
    text-transform: uppercase;
  }
  .title--artist {
    font-size: 186px;
    filter: drop-shadow(0 0 6px var(--glow-violet)) drop-shadow(0 0 16px var(--glow-violet));
  }
  .title--track {
    font-size: 128px;
    filter: drop-shadow(0 0 6px var(--glow-cyan)) drop-shadow(0 0 16px var(--glow-cyan));
  }
</style>
</head>
<body>
  <main class="cover">
    <div class="cover-art" role="img" aria-label="Speaker cone photographed glowing cyan, floating in a starry violet and blue nebula"></div>
    <svg class="titles" viewBox="0 0 1199 1200" xmlns="http://www.w3.org/2000/svg">
      <text class="title title--artist" x="599" y="345" text-anchor="middle" textLength="1045" lengthAdjust="spacingAndGlyphs">Dj Lumbrix</text>
      <text class="title title--track" x="605" y="1075" text-anchor="middle" textLength="1030" lengthAdjust="spacingAndGlyphs">Velvet Tideway</text>
    </svg>
  </main>
</body>
</html>
```